Design of an attractive membership brochure/membership card for an Electrical Business

Hi, we are an electrical business based in Sydney, Australia.

Our design's aim is to attract and target new customers into using our business as a repeat for anything electrical in their home. We would be handing this out to them after a job is completed and they're happy with the service.
We're thinking of a brochure, possibly additional membership cards with personalized number ID's for each client.

Open to ideas, but some of the things we want to include on our brochure are perks of why the client should sign up with us as a lifetime client
- Discounted emergency call out fees outside of normal hours
- Lifetime membership price, one time payment
- Exclusive 10% member discount on all future jobs
- Priority on any during business hour jobs or emergencies

If any other questions please don't hesitate to reach out.
We've attached our logo for reference for the mock designs.
Our website
https://brightwirecrew.com.au/

```html
<!DOCTYPE html>
<html lang="en">
<head>
<meta charset="utf-8">
<title>Bright Wire Crew – Membership Brochure</title>
<link rel="stylesheet" href="https://fonts.googleapis.com/css2?family=Libre+Baskerville:ital,wght@0,400;0,700;1,400;1,700&family=Open+Sans:ital,wght@0,400;0,700;1,400&display=swap">
<style>
  :root {
    --stage: #a6a6a6;
    --paper: #e9e9e9;
    --ink: #111111;
    --night: #1c1c1c;
    --red: #d42d20;
    --red-deep: #b3221a;
    --field: #b1b1b1;
    --white: #ffffff;
  }
  * { box-sizing: border-box; margin: 0; padding: 0; }
  html, body { width: 1200px; height: 2179px; overflow: hidden; }
  body { background: var(--stage); position: relative; font-family: "Open Sans", sans-serif; color: var(--ink); }

  .side-label {
    position: absolute; left: 40px; width: 120px;
    font-family: "Libre Baskerville", serif; font-style: italic; font-weight: 700;
    font-size: 112px; color: var(--white); letter-spacing: 2px;
    writing-mode: vertical-rl; transform: rotate(180deg);
    display: flex; align-items: center; justify-content: center;
    text-shadow: 3px 3px 6px rgba(0,0,0,.35);
  }
  .side-label--front { top: 300px; height: 683px; }
  .side-label--inside { top: 1130px; height: 683px; }

  .panel {
    position: absolute; left: 178px; width: 958px; height: 683px;
    background: var(--paper); overflow: hidden;
    box-shadow: 6px 8px 14px rgba(0,0,0,.35);
  }
  .panel--front { top: 300px; }
  .panel--inside { top: 1130px; }
  .panel-art { position: absolute; inset: 0; }

  .brand-title {
    position: absolute; left: 22px; top: 40px;
    font-family: "Libre Baskerville", serif; font-style: italic; font-weight: 700;
    font-size: 34px; color: var(--white); letter-spacing: .5px; white-space: nowrap;
  }
  .brand-tagline {
    position: absolute; left: 22px; top: 82px;
    font-style: italic; font-size: 21px; color: var(--red); white-space: nowrap;
  }
  .brand-rule { position: absolute; left: 22px; top: 113px; width: 320px; height: 3px;
    background: linear-gradient(90deg, var(--red) 0 52%, var(--white) 52% 100%); }

  .brand-mark {
    position: absolute; font-weight: 700; color: var(--red);
    line-height: 1.05; letter-spacing: 2px; white-space: nowrap;
  }
  .brand-mark--front { right: 22px; top: 40px; text-align: right; font-size: 26px; }
  .brand-mark--inside { left: 26px; top: 142px; font-size: 20px; }

  .perks-kicker {
    position: absolute; left: 22px; top: 292px;
    font-family: "Libre Baskerville", serif; font-style: italic; font-weight: 700;
    font-size: 25px; color: var(--red);
  }
  .perks-heading {
    position: absolute; left: 22px; top: 325px;
    font-family: "Libre Baskerville", serif; font-style: italic; font-weight: 700;
    font-size: 42px; color: var(--ink);
  }
  .perks-rule { position: absolute; left: 22px; top: 382px; width: 320px; height: 3px;
    background: linear-gradient(90deg, var(--red) 0 50%, var(--ink) 50% 100%); }

  .perk-list { position: absolute; left: 20px; top: 425px; width: 480px; list-style: none; }
  .perk { display: flex; align-items: center; gap: 10px; font-size: 17.5px; line-height: 1.15; min-height: 44px; margin-bottom: 5px; }
  .perk-icon { flex: none; width: 42px; height: 42px; }

  .about-heading {
    position: absolute; left: 22px; top: 308px;
    font-family: "Libre Baskerville", serif; font-style: italic; font-weight: 700;
    font-size: 36px; line-height: 1.3;
  }
  .about-heading .accent { color: var(--red); }
  .about-rule { position: absolute; left: 24px; top: 398px; width: 276px; height: 3px;
    background: linear-gradient(90deg, var(--red) 0 50%, var(--ink) 50% 100%); }
  .about-copy { position: absolute; left: 20px; top: 420px; width: 420px; font-size: 13.2px; line-height: 1.22; }
  .about-copy p + p { margin-top: 16px; }

  .form-page { position: absolute; left: 472px; top: 0; width: 486px; height: 683px; background: var(--paper);
    box-shadow: inset 8px 0 10px -6px rgba(0,0,0,.35); }
  .form-title {
    position: absolute; left: 0; right: 0; top: 14px; text-align: center;
    font-family: "Libre Baskerville", serif; font-style: italic; font-weight: 700; font-size: 30px;
  }
  .form-title .accent { color: var(--red); }
  .form-title-rule { position: absolute; left: 80px; top: 55px; width: 332px; height: 3px;
    background: linear-gradient(90deg, var(--red) 0 72%, var(--ink) 72% 100%); }
  .form-field { position: absolute; left: 27px; width: 398px; }
  .form-label { font-family: "Libre Baskerville", serif; font-style: italic; font-weight: 700; font-size: 17px; line-height: 1; margin-bottom: 10px; }
  .form-box { height: 49px; background: var(--field); }
  .form-box + .form-box { margin-top: 5px; }
</style>
</head>
<body>

<div class="side-label side-label--front">FRONT</div>
<div class="side-label side-label--inside">INSIDE</div>

<section class="panel panel--front">
  <svg class="panel-art" viewBox="0 0 958 683">
    <defs>
      <linearGradient id="night-fade" x1="0" y1="0" x2="1" y2="1">
        <stop offset="0" stop-color="#2a2a2a"/><stop offset="1" stop-color="#0d0d0d"/>
      </linearGradient>
      <radialGradient id="bulb-glow" cx="0.6" cy="0.45" r="0.7">
        <stop offset="0" stop-color="#6b5a45"/><stop offset=".45" stop-color="#2a2d36"/><stop offset="1" stop-color="#0c0e14"/>
      </radialGradient>
      <linearGradient id="house-tone" x1="0" y1="0" x2="0" y2="1">
        <stop offset="0" stop-color="#8b93b3"/><stop offset=".6" stop-color="#5d647c"/><stop offset="1" stop-color="#3a3f4d"/>
      </linearGradient>
      <linearGradient id="band-red" x1="0" y1="0" x2="1" y2="1">
        <stop offset="0" stop-color="#c0251b"/><stop offset="1" stop-color="#d9362a"/>
      </linearGradient>
    </defs>
    <polygon points="0,0 958,0 958,420 740,520 260,215 0,300" fill="url(#night-fade)"/>
    <polygon points="440,0 958,0 958,150 740,295 440,160" fill="url(#bulb-glow)" role="img" aria-label="Photo of glowing filament light bulbs hanging in the dark"/>
    <polygon points="330,118 740,295 740,520 260,215" fill="url(#band-red)"/>
    <text transform="translate(460,270) rotate(25)" font-family="Libre Baskerville, serif" font-size="36" fill="#a81f17" opacity=".8">
      <tspan x="40" y="0">ELECTRICAL</tspan><tspan x="0" y="42">EXPERT</tspan>
    </text>
    <polygon points="378,683 958,420 958,683" fill="url(#house-tone)" role="img" aria-label="Photo of a suburban house with lit windows at dusk"/>
  </svg>

  <div class="brand-title">BRIGHT WIRE CREW</div>
  <div class="brand-tagline">Sydney-based electrical business</div>
  <div class="brand-rule"></div>
  <div class="brand-mark brand-mark--front">BRIGHT WIRE<br>CREW</div>

  <div class="perks-kicker">Perks of Signing up as a</div>
  <div class="perks-heading">Lifetime Client:</div>
  <div class="perks-rule"></div>

  <ul class="perk-list">
    <li class="perk">
      <svg class="perk-icon" viewBox="0 0 42 42"><circle cx="21" cy="21" r="20" fill="#222"/><circle cx="21" cy="21" r="12" fill="none" stroke="#d42d20" stroke-width="1.5"/><path d="M15 17c2 5 5 8 10 10l2-3-3-2-2 1c-2-1-3-2-4-4l1-2-2-3z" fill="#d42d20"/></svg>
      <span>Discounted emergency call out fees outside<br>of normal hours</span>
    </li>
    <li class="perk">
      <svg class="perk-icon" viewBox="0 0 42 42"><circle cx="21" cy="21" r="20" fill="#222"/><rect x="14" y="12" width="14" height="18" fill="none" stroke="#d42d20" stroke-width="1.5"/><path d="M17 17h8M17 21h8M17 25h5" stroke="#d42d20" stroke-width="1.5"/></svg>
      <span>Lifetime membership price, one-time payment</span>
    </li>
    <li class="perk">
      <svg class="perk-icon" viewBox="0 0 42 42"><circle cx="21" cy="21" r="20" fill="#222"/><path d="M12 24l10-10h8v8L20 32z" fill="none" stroke="#d42d20" stroke-width="1.5"/><circle cx="26" cy="18" r="1.6" fill="#d42d20"/></svg>
      <span>Exclusive 10% member discount on all future jobs</span>
    </li>
    <li class="perk">
      <svg class="perk-icon" viewBox="0 0 42 42"><circle cx="21" cy="21" r="20" fill="#222"/><rect x="12" y="13" width="18" height="5" fill="none" stroke="#d42d20" stroke-width="1.5"/><rect x="12" y="19" width="18" height="5" fill="none" stroke="#d42d20" stroke-width="1.5"/><rect x="12" y="25" width="18" height="5" fill="none" stroke="#d42d20" stroke-width="1.5"/></svg>
      <span>Priority on any during business hour jobs or<br>emergencies</span>
    </li>
  </ul>
</section>

<section class="panel panel--inside">
  <svg class="panel-art" viewBox="0 0 958 683">
    <defs>
      <linearGradient id="night-fade-2" x1="0" y1="0" x2="1" y2="1">
        <stop offset="0" stop-color="#2a2a2a"/><stop offset="1" stop-color="#0d0d0d"/>
      </linearGradient>
      <radialGradient id="bulb-glow-2" cx="0.5" cy="0.3" r="0.8">
        <stop offset="0" stop-color="#6b5a45"/><stop offset="1" stop-color="#0c0e14"/>
      </radialGradient>
    </defs>
    <polygon points="0,0 472,0 472,360 240,215 0,300" fill="url(#night-fade-2)"/>
    <polygon points="390,0 472,0 472,200 390,164" fill="url(#bulb-glow-2)" role="img" aria-label="Photo of glowing filament light bulbs"/>
    <polygon points="300,125 472,200 472,360 240,215" fill="#c9291e"/>
  </svg>

  <div class="brand-title">BRIGHT WIRE CREW</div>
  <div class="brand-tagline">Sydney-based electrical business</div>
  <div class="brand-rule"></div>
  <div class="brand-mark brand-mark--inside">BRIGHT WIRE<br>CREW</div>

  <h2 class="about-heading"><span class="accent">About Us -</span><br>Bright Wire Crew</h2>
  <div class="about-rule"></div>
  <div class="about-copy">
    <p>Bright Wire Crew is a Sydney-based electrical business specialising in electrical maintenance work for residential, commercial, strata and real estate clients. It began with two mates with a strong desire to change the image of tradies and provide exceptional service. As a team of electricians based in the Inner West of Sydney, we understand the need of everyday people struggling to find good, reliable and trustworthy electricians.</p>
    <p>At Bright Wire Crew, we have high expectations of ourselves and strive to improve every day. We're always available around the clock to provide professional advice or give a helping hand when in need.</p>
  </div>

  <div class="form-page">
    <h2 class="form-title"><span class="accent">MEMBERSHIP</span> FORM</h2>
    <div class="form-title-rule"></div>
    <div class="form-field" style="top:133px"><div class="form-label">FULL NAME</div><div class="form-box"></div></div>
    <div class="form-field" style="top:238px"><div class="form-label">ID NUMBER</div><div class="form-box"></div></div>
    <div class="form-field" style="top:330px"><div class="form-label">COMPLETE ADDRESS</div><div class="form-box"></div><div class="form-box"></div></div>
    <div class="form-field" style="top:477px"><div class="form-label">EMAIL</div><div class="form-box"></div></div>
    <div class="form-field" style="top:571px"><div class="form-label">PHONE NUMBER</div><div class="form-box"></div></div>
  </div>
</section>

</body>
</html>
```